New Manager Resource Guide & Planner

I need a template designed for a resource guide and planner that new managers would use to help guide them their first year managing others. Think your typical planner injected with tips, worksheets, quotes and other helpful tools. Initially, I'd like a template created for some key pages: one month, one week and single day layouts plus a quote page. I'm attaching a very rudimentary idea of the project, just need it purposefully designed with my colors and branding. The size is 6" x 8 " h. I would like this done in InDesign or Keynote so I can edit it and create other pages. Most likely, though, will contract you to finish out the entire project.

Target Market(s)

new managers (and HR directors who will most likely purchase the resource planner for their employees)

Industry/Entity Type

Advertising

Font styles to use
Other font styles liked:
• archer, open sans

Requirements
Must have
• a creative feel to it (I come from the advertising industry, so a fun design is OK). use of my branding and colors, be noticeably well designed.
Nice to have
• look at other planners for ideas. my goal is to use your template to build out the other pages I need. So think cool edging, or stylized quote boxes, etc.
Should not have
• please use the colors in my palette in the attached pdf plus any other complementary colors you see fit. my branding uses the font archer, open sans, use these and any other fonts that you see fit.

```html
<!DOCTYPE html>
<html lang="en">
<head>
<meta charset="utf-8">
<title>New Manager Resource Guide &amp; Planner – Page Templates</title>
<link href="https://fonts.googleapis.com/css2?family=Open+Sans:ital,wght@0,400;0,600;0,700;1,400&display=swap" rel="stylesheet">
<style>
  :root{
    --purple:#5b3795;
    --lime:#e2e65c;
    --lime-deep:#c3cc2e;
    --olive:#8a8a33;
    --lavender:#d3c9e6;
    --lime-pale:#f2f5cf;
    --beige:#e3dccb;
    --ink:#222;
    --rule:#6d6d6d;
    --grid:#c9bfdc;
    --tag:#bdbdbd;
  }
  *{box-sizing:border-box;margin:0;padding:0}
  html,body{width:1200px;height:1200px;overflow:hidden;background:#fff}
  body{position:relative;font-family:"Open Sans",Arial,sans-serif;color:var(--ink)}
  ul{list-style:none}

  .page{position:absolute;overflow:hidden}
  .page-framed{background:var(--purple)}
  .page-plain{background:#fff;box-shadow:0 0 6px rgba(0,0,0,.12)}
  .sheet{position:absolute;inset:6px;background:#fff}
  .decor{position:absolute;left:0;top:0;pointer-events:none}
  .abs{position:absolute}

  /* positions */
  .daily-tasks{left:37px;top:114px;width:368px;height:489px}
  .weekly{left:427px;top:114px;width:365px;height:485px}
  .daily-sales{left:816px;top:114px;width:364px;height:485px}
  .month{left:37px;top:674px;width:366px;height:488px}
  .month-focus{left:427px;top:674px;width:365px;height:488px}
  .quote-page{left:816px;top:674px;width:364px;height:488px}

  /* daily header */
  .lime-block{left:6px;top:6px;width:184px;height:79px;background:var(--lime)}
  .date-chip{left:78px;top:26px;width:39px;height:27px;background:var(--purple);color:#fff;font-weight:700;font-size:16px;line-height:27px;text-align:center}
  .day-name,.month-name{top:69px;font-size:10.5px}
  .day-name{left:20px}
  .month-name{left:140px}
  .quote-small{left:198px;top:20px;width:164px;font-style:italic;font-size:10.5px;line-height:16px;color:var(--purple);text-align:center}

  .band{background:var(--purple);color:#fff;font-weight:700;font-size:8px;letter-spacing:.2px}
  .band-top{left:6px;right:6px;top:87px;height:20px;line-height:20px}
  .band-top span{position:absolute}
  .col-rule{background:#111;width:1px}

  .schedule{left:6px;width:176px}
  .schedule li{height:22px;border-bottom:1px dotted var(--rule);font-size:9.5px;display:flex;align-items:flex-end;padding:0 0 1px 4px}
  .todo{left:192px;width:170px}
  .todo li{height:22px;border-bottom:1px dotted var(--rule);display:flex;align-items:flex-end;padding:0 0 3px 2px}
  .check{width:10px;height:10px;border:1px solid var(--purple);background:#fff}
  .foot-band{height:15px;line-height:15px;padding-left:5px;font-size:9px}

  /* sales daily */
  .goal-label{left:192px;top:9px;font-size:10px}
  .head-rule{left:6px;right:6px;top:84px;height:3px;background:var(--purple)}
  .section-label{font-weight:700;font-size:8px}
  .sales{left:188px;top:112px;width:170px}
  .sales li{height:15.5px;border-bottom:1px dotted var(--rule);display:flex;align-items:center;padding-left:4px}
  .ring{width:9px;height:9px;border:1px solid var(--purple);border-radius:50%;background:#fff}
  .notes-label{left:188px;top:340px;font-size:9.5px}
  .notes-lines{left:188px;right:6px;top:354px;bottom:6px;background:radial-gradient(circle,#777 .7px,transparent .9px) 0 8px/3px 17px repeat}

  /* weekly */
  .week-title{right:16px;top:18px;font-weight:700;font-size:9.5px}
  .week-rule{left:6px;right:6px;top:32px;height:3px;background:var(--purple)}
  .days{left:14px;right:7px;top:39px}
  .day{height:70.6px;border-bottom:1px solid #8d8d8d;position:relative}
  .day:last-child{border-bottom:none}
  .day-head{display:flex;align-items:center;height:28px;font-size:10.5px}
  .day-dot{width:26px;height:26px;border-radius:50%;background:var(--olive);color:#fff;font-size:10px;line-height:26px;text-align:center;margin-right:5px}
  .day-line{height:12.5px;border-bottom:1px dotted var(--rule)}
  .week-foot{left:6px;right:6px;top:470px;height:3px;background:#fff}

  /* month */
  .month-head{left:6px;top:6px;width:352px;height:31px;background:var(--lime-deep)}
  .month-head h2{position:absolute;left:6px;top:4px;font-size:17px;font-weight:700;letter-spacing:.2px}
  .month-head span{position:absolute;right:7px;top:9px;font-size:10.5px}
  .weekdays{left:10px;top:38px;width:345px;height:21px;display:grid;grid-template-columns:repeat(7,1fr);background:var(--purple)}
  .weekdays span{color:#fff;font-weight:700;font-size:10px;text-align:center;line-height:21px;border-left:1px solid #fff}
  .weekdays span:first-child{border-left:none}
  .cal{left:10px;top:59px;width:345px;height:342px;display:grid;grid-template-columns:repeat(7,1fr);grid-template-rows:repeat(6,1fr);border-left:1px solid var(--grid)}
  .cal div{border-right:1px solid var(--grid);border-bottom:1px solid var(--grid);position:relative}
  .cal b{position:absolute;left:3px;top:2px;width:13px;height:8px;background:var(--tag);font-weight:400;font-size:6px;line-height:8px;text-align:center}
  .month-rule{left:10px;top:400px;width:345px;height:3px;background:var(--purple)}
  .month-notes{left:20px;top:411px;font-weight:700;font-size:10.5px;color:var(--purple)}
  .note-line{height:1px;background:#333}

  /* month focus */
  .focus-title{left:7px;top:6px;font-weight:700;font-size:9.5px}
  .focus-rule{left:6px;right:6px;top:20px;height:2px;background:var(--purple)}
  .big-picture{left:6px;top:23px;width:180px;height:52px;background:var(--lime);padding:2px 2px 0 2px}
  .mini-label{font-size:6.5px}
  .big-picture .lines{position:absolute;left:2px;right:6px;top:10px;height:40px;background:radial-gradient(circle,#555 .6px,transparent .8px) 0 5px/3px 11px repeat}
  .minical{top:27px;width:70px}
  .minical p{font-size:3.5px;text-align:center;font-weight:700}
  .minical .g{height:42px;margin-top:2px;border:.5px solid #bbb;background:
      linear-gradient(#bbb .5px,transparent .5px) 0 0/100% 7px,
      linear-gradient(90deg,#bbb .5px,transparent .5px) 0 0/10px 100%}
  .focus-vrule{left:186px;top:23px;bottom:0;width:1px;background:var(--purple)}
  .focus-hrule{left:6px;right:6px;top:76px;height:1px;background:var(--purple)}
  .todo-lines{left:6px;top:86px;width:174px;bottom:12px;background:radial-gradient(circle,#666 .6px,transparent .8px) 0 6px/3px 14px repeat}
  .todo-vdots{left:18px;top:96px;bottom:12px;width:1px;background:radial-gradient(circle,#666 .6px,transparent .8px) 0 0/1px 3px repeat-y}
  .focus-section{left:187px;right:6px}
  .focus-section .mini-label{padding:4px 0 0 4px}
  .focus-section .lines{position:absolute;left:0;right:0;top:14px;bottom:4px;background:radial-gradient(circle,#666 .6px,transparent .8px) 0 6px/3px 14px repeat}
  .focus-section + .focus-section{border-top:1px solid var(--purple)}

  /* quote page */
  .quote-circle{left:57px;top:16px;width:248px;height:248px;border-radius:50%;background:var(--lime);display:flex;align-items:center;justify-content:center;text-align:center}
  .quote-circle p{font-weight:700;font-size:19.5px;line-height:31px;color:#1d1d1d;margin-top:-24px}
  .quote-lines{left:36px;width:280px;top:318px;height:72px;background:radial-gradient(circle,rgba(255,255,255,.75) .6px,transparent .8px) 0 0/3px 12.8px repeat}
  .quote-box{left:6px;top:413px;width:352px;height:68px;background:#fff}
</style>
</head>
<body>

<!-- Daily page: schedule + to-do -->
<section class="page page-framed daily-tasks">
  <div class="sheet"></div>
  <svg class="decor" width="368" height="489" aria-hidden="true">
    <circle cx="127" cy="232" r="116" fill="var(--lavender)"/>
    <circle cx="277" cy="342" r="34" fill="var(--lime-pale)"/>
  </svg>
  <div class="abs lime-block"></div>
  <div class="abs date-chip">19</div>
  <div class="abs day-name">Tuesday</div>
  <div class="abs month-name">March</div>
  <p class="abs quote-small">Treat Employees like they make a difference and they will.</p>
  <div class="abs band band-top"><span style="left:5px">Toda'y Schedule:</span><span style="left:190px">To Do:</span></div>
  <div class="abs col-rule" style="left:190px;top:85px;bottom:6px"></div>
  <ul class="abs schedule" style="top:108px">
    <li>8:00</li><li>9:00</li><li>10:00</li><li>11:00</li><li>12:00</li><li>1:00</li><li>2:00</li>
    <li>3:00</li><li>4:00</li><li>5:00</li><li>6:00</li><li>6:00</li><li>7:00</li><li>8:00</li>
  </ul>
  <ul class="abs todo" style="top:108px">
    <li><span class="check"></span></li><li><span class="check"></span></li><li><span class="check"></span></li>
    <li><span class="check"></span></li><li><span class="check"></span></li><li><span class="check"></span></li>
    <li><span class="check"></span></li><li><span class="check"></span></li><li><span class="check"></span></li>
    <li><span class="check"></span></li><li><span class="check"></span></li><li><span class="check"></span></li>
    <li><span class="check"></span></li><li><span class="check"></span></li>
  </ul>
  <div class="abs band foot-band" style="left:6px;top:422px;width:176px">TONIGHT</div>
  <div class="abs band foot-band" style="left:192px;top:424px;width:170px">GRATITUDE</div>
</section>

<!-- Weekly page -->
<section class="page page-framed weekly">
  <div class="sheet" style="bottom:15px"></div>
  <svg class="decor" width="365" height="485" aria-hidden="true">
    <circle cx="177" cy="184" r="114" fill="var(--lavender)"/>
    <circle cx="238" cy="344" r="34" fill="var(--lime-pale)"/>
  </svg>
  <div class="abs week-title">March 2019</div>
  <div class="abs week-rule"></div>
  <div class="abs days">
    <div class="day"><div class="day-head"><span class="day-dot">18</span>Monday</div><div class="day-line"></div><div class="day-line"></div><div class="day-line"></div></div>
    <div class="day"><div class="day-head"><span class="day-dot">19</span>Tuesday</div><div class="day-line"></div><div class="day-line"></div><div class="day-line"></div></div>
    <div class="day"><div class="day-head"><span class="day-dot">20</span>Wednesday</div><div class="day-line"></div><div class="day-line"></div><div class="day-line"></div></div>
    <div class="day"><div class="day-head"><span class="day-dot">21</span>Thusday</div><div class="day-line"></div><div class="day-line"></div><div class="day-line"></div></div>
    <div class="day"><div class="day-head"><span class="day-dot">21</span>Friday</div><div class="day-line"></div><div class="day-line"></div><div class="day-line"></div></div>
    <div class="day"><div class="day-head"><span class="day-dot">22</span>Saturday</div><div class="day-line"></div><div class="day-line"></div><div class="day-line"></div></div>
  </div>
  <div class="abs week-foot"></div>
</section>

<!-- Daily page: schedule + sales activity -->
<section class="page page-framed daily-sales">
  <div class="sheet"></div>
  <svg class="decor" width="364" height="485" aria-hidden="true">
    <circle cx="245" cy="216" r="114" fill="var(--lavender)"/>
    <circle cx="40" cy="371" r="34" fill="var(--lavender)"/>
    <circle cx="56" cy="141" r="16" fill="var(--lime-pale)"/>
    <circle cx="226" cy="404" r="16" fill="var(--beige)"/>
  </svg>
  <div class="abs lime-block" style="width:176px;height:78px"></div>
  <div class="abs date-chip">19</div>
  <div class="abs day-name">Tuesday</div>
  <div class="abs month-name" style="left:140px">March</div>
  <div class="abs goal-label">Daily Goal</div>
  <div class="abs head-rule"></div>
  <div class="abs" style="left:182px;top:84px;bottom:6px;width:2px;background:var(--purple)"></div>
  <div class="abs section-label" style="left:10px;top:92px">Toda'y Schedule:</div>
  <div class="abs section-label" style="left:191px;top:92px">Sales Activity:</div>
  <ul class="abs schedule" style="top:106px">
    <li>8:00</li><li>9:00</li><li>10:00</li><li>11:00</li><li>12:00</li><li>1:00</li><li>2:00</li>
    <li>3:00</li><li>4:00</li><li>5:00</li><li>6:00</li><li>6:00</li><li>7:00</li><li>8:00</li>
  </ul>
  <ul class="abs sales">
    <li><span class="ring"></span></li><li><span class="ring"></span></li><li><span class="ring"></span></li>
    <li><span class="ring"></span></li><li><span class="ring"></span></li><li><span class="ring"></span></li>
    <li><span class="ring"></span></li><li><span class="ring"></span></li><li><span class="ring"></span></li>
    <li><span class="ring"></span></li><li><span class="ring"></span></li><li><span class="ring"></span></li>
    <li><span class="ring"></span></li><li><span class="ring"></span></li>
  </ul>
  <div class="abs" style="left:184px;right:6px;top:334px;height:1px;background:#222"></div>
  <div class="abs notes-label">Notes</div>
  <div class="abs notes-lines"></div>
  <div class="abs todo-vdots" style="left:201px;top:356px"></div>
  <div class="abs band foot-band" style="left:6px;top:418px;width:174px">TONIGHT</div>
</section>

<!-- Month at a glance -->
<section class="page page-plain month">
  <svg class="decor" width="366" height="488" aria-hidden="true">
    <circle cx="89" cy="186" r="74" fill="var(--lavender)" opacity=".8"/>
    <circle cx="276" cy="377" r="74" fill="var(--lavender)" opacity=".8"/>
  </svg>
  <header class="abs month-head"><h2>MONTH AT A GLANCE</h2><span>March</span></header>
  <div class="abs weekdays"><span>Mon</span><span>Tue</span><span>Wed</span><span>Thu</span><span>Fri</span><span>Sat</span><span>Sun</span></div>
  <div class="abs cal">
    <div></div><div></div><div></div><div></div><div></div><div><b>01</b></div><div><b>02</b></div>
    <div><b>03</b></div><div><b>04</b></div><div><b>05</b></div><div><b>06</b></div><div><b>07</b></div><div><b>08</b></div><div><b>09</b></div>
    <div><b>10</b></div><div><b>11</b></div><div><b>12</b></div><div><b>13</b></div><div><b>14</b></div><div><b>15</b></div><div><b>16</b></div>
    <div><b>17</b></div><div><b>18</b></div><div><b>19</b></div><div><b>20</b></div><div><b>21</b></div><div><b>22</b></div><div><b>23</b></div>
    <div><b>24</b></div><div><b>25</b></div><div><b>26</b></div><div><b>27</b></div><div><b>28</b></div><div><b>29</b></div><div><b>30</b></div>
    <div><b>31</b></div><div></div><div></div><div></div><div></div><div></div><div></div>
  </div>
  <div class="abs month-rule"></div>
  <div class="abs month-notes">Notes</div>
  <div class="abs note-line" style="left:68px;width:321px;top:428px;width:321px;right:14px;width:auto"></div>
  <div class="abs note-line" style="left:20px;right:14px;top:449px"></div>
  <div class="abs note-line" style="left:20px;right:14px;top:469px"></div>
</section>

<!-- Month focus page -->
<section class="page page-plain month-focus">
  <svg class="decor" width="365" height="488" aria-hidden="true">
    <circle cx="177" cy="226" r="114" fill="var(--lavender)"/>
    <circle cx="238" cy="386" r="34" fill="var(--lime-pale)"/>
  </svg>
  <div class="abs focus-title">March 2019</div>
  <div class="abs focus-rule"></div>
  <div class="abs big-picture"><p class="mini-label">Big Picture</p><div class="lines"></div></div>
  <div class="abs minical" style="left:198px"><p>March 2019</p><div class="g"></div></div>
  <div class="abs minical" style="left:277px"><p>April 2019</p><div class="g"></div></div>
  <div class="abs focus-vrule"></div>
  <div class="abs focus-hrule"></div>
  <div class="abs mini-label" style="left:8px;top:80px">To Do:</div>
  <div class="abs todo-lines"></div>
  <div class="abs todo-vdots"></div>
  <div class="abs focus-section" style="top:77px;height:109px"><p class="mini-label">Deadlines</p><div class="lines"></div></div>
  <div class="abs focus-section" style="top:186px;height:112px;border-top:1px solid var(--purple)"><p class="mini-label">Financial</p><div class="lines"></div></div>
  <div class="abs focus-section" style="top:298px;height:110px;border-top:1px solid var(--purple)"><p class="mini-label">Project</p><div class="lines"></div></div>
  <div class="abs focus-section" style="top:408px;height:74px;border-top:1px solid var(--purple)"><p class="mini-label">Other</p><div class="lines"></div></div>
</section>

<!-- Quote page -->
<section class="page page-framed quote-page">
  <div class="abs quote-circle"><p>Treat Employees like<br>they make a difference<br>and they will.</p></div>
  <div class="abs quote-lines"></div>
  <div class="abs quote-box"></div>
</section>

</body>
</html>
```